Bellhaven Select Business Card Design Project

About the company: Here at Marigrove Essence, we focus on cosmetic products that based on essential oils and different kinds of plant essences. All of our raw materials are pure organic and specially selected from local producers in Australia.

I'm here to look for a unique business card design, to replace the current one later on, so I don't have many requirements. Why I wanna restrict designers' creativity?

All I know is: 1. do not make it too complicated, straight forward, simple and pure. 2. this design may be used for other purposes (i.e. logo and slogan on the front, Brand Story and contact details at the back). Therefor, I'd like to have the design for 3 layouts, one only have logo, slogan, contact detials, one for the brand story, the other one for the personal business card with staff's mob etc...

A vector graphic is required, i.e. eps, ai, easy for me to resize.

Round Corner.

Thanks
Updates

Plz add "Hand made in Australia" in the design, cheers.

Target Market(s)

Women aged yr 20-50

Industry/Entity Type

Business

Requirements
Must have
• Logo: please see attacment (eps, ai)

Slogan: Dew Touched Delight

Website:www.marigroveessence-demo.com.au

Address: temporary not available

Phone: temporary not available

"Hand made in Australia"

Nice to have
• Prefer round corner

```html
<!DOCTYPE html>
<html lang="en">
<head>
<meta charset="utf-8">
<title>Marigrove Essence – Business Card</title>
<link href="https://fonts.googleapis.com/css2?family=Didact+Gothic&family=Dancing+Script:wght@400;500&display=swap" rel="stylesheet">
<style>
  :root {
    --backdrop: #d9d9db;
    --card: #f4f4f2;
    --rose: #e0466e;
    --ink: #3a3a3a;
    --ink-soft: #555555;
  }
  * { margin: 0; padding: 0; box-sizing: border-box; }
  html, body {
    width: 1200px;
    height: 1006px;
    overflow: hidden;
    background: var(--backdrop);
  }
  .card {
    position: absolute;
    left: 100px;
    top: 217px;
    width: 1000px;
    height: 572px;
    background: var(--card);
    border-radius: 28px;
    box-shadow: 0 10px 30px rgba(0, 0, 0, 0.18);
    font-family: "Didact Gothic", "Century Gothic", sans-serif;
    color: var(--ink);
  }
  .brand {
    position: absolute;
    left: 250px;
    top: 60px;
    display: flex;
    align-items: center;
    gap: 18px;
  }
  .brand-mark {
    width: 34px;
    height: 34px;
    border-radius: 50%;
    background: var(--rose);
  }
  .brand-name {
    font-family: "Didact Gothic", "Century Gothic", sans-serif;
    font-size: 58px;
    color: var(--rose);
    letter-spacing: 1px;
    line-height: 1;
  }
  .slogan {
    position: absolute;
    left: 520px;
    top: 178px;
    font-family: "Dancing Script", cursive;
    font-size: 34px;
    color: var(--rose);
  }
  .address {
    position: absolute;
    left: 650px;
    top: 290px;
    font-size: 22px;
    line-height: 1.45;
    color: var(--ink-soft);
  }
  .contact {
    position: absolute;
    left: 70px;
    top: 330px;
    font-size: 30px;
    line-height: 1.3;
    color: var(--ink-soft);
  }
  .contact .website {
    color: var(--rose);
    font-weight: 700;
    font-size: 29px;
  }
  .tagline {
    position: absolute;
    left: 0;
    right: 0;
    top: 462px;
    text-align: center;
    font-family: "Dancing Script", cursive;
    font-size: 46px;
    color: var(--ink);
  }
</style>
</head>
<body>
  <main class="card">
    <div class="brand">
      <span class="brand-mark" aria-hidden="true"></span>
      <span class="brand-name">Marigrove Essence</span>
    </div>
    <p class="slogan">Dew Touched Delight</p>
    <address class="address">
      Kestrel Works, Alder Road<br>
      Northfield, NF4 7QA
    </address>
    <div class="contact">
      <p class="phone">+441134960712</p>
      <p class="email">jordan.ellery@mail-demo.com</p>
      <p class="website">www.marigroveessence-demo.com.au</p>
    </div>
    <p class="tagline">Hand made in Australia</p>
  </main>
</body>
</html>
```